KBMR new business card design

We need a business card design for our established business which is Australia wide however based in Melbourne. We are a young team of Financial Planners who specialize in Insurance and Basic super advice for people like us.

We are people who help our clients get things done in a timely and cost effective manner whilst having a good time and a laugh along the way.

We would like this to have a consistent feel with our new e-brochure which i have attached from a color and font perspective.

Industry/Entity Type

Business

Requirements
Must have
• We do not need specific address details rather just the states we are in:

VIC/NSW/QLD/TAS
Nice to have
• Curved edge to mate the brochure

```html
<!DOCTYPE html>
<html lang="en">
<head>
<meta charset="utf-8">
<title>KBMR business cards</title>
<link rel="stylesheet" href="https://fonts.googleapis.com/css2?family=Arimo:wght@400;700&display=swap">
<style>
  :root {
    --stage: #f2f2f2;
    --charcoal: #231f20;
    --charcoal-warm: #4a4243;
    --paper: #f4f4f4;
    --paper-shade: #dcdcdc;
    --green: #6cc04a;
    --green-bright: #4be34f;
    --grey-text: #8a8a8a;
    --grey-text-dark: #7a7a7a;
    --ink: #141414;
    --white: #ffffff;
  }
  * { box-sizing: border-box; margin: 0; padding: 0; }
  html, body {
    width: 1056px; height: 1200px; overflow: hidden;
    background: var(--stage);
    font-family: "Arimo", Arial, sans-serif;
  }
  .sheet { position: relative; width: 1056px; height: 1200px; }

  .card {
    position: absolute; width: 560px; height: 320px; overflow: hidden;
    box-shadow: 0 6px 18px rgba(0,0,0,.18);
  }
  .card--dark-left  { left: 158px; top: 70px; }
  .card--light-left { left: 440px; top: 440px; }
  .card--green-right{ left: 140px; top: 810px; }

  .card__shapes { position: absolute; inset: 0; width: 100%; height: 100%; }

  .brand {
    position: absolute; left: 48px; top: 66px; width: 130px;
    display: flex; flex-direction: column; align-items: center; gap: 18px;
  }
  .brand__square { width: 96px; height: 96px; background: var(--green); }
  .brand__name { font-size: 32px; font-weight: 700; letter-spacing: .5px; line-height: 1; }
  .card--dark-left .brand__name,
  .card--green-right .brand__name { color: var(--white); }
  .card--light-left .brand__name { color: var(--ink); }

  .states {
    position: absolute; left: 205px; top: 52px; list-style: none;
    font-size: 21px; font-weight: 700; line-height: 28px;
  }
  .states li::before { content: "\203A"; margin-right: 8px; }
  .email {
    position: absolute; left: 208px; top: 185px;
    font-size: 19px; font-weight: 700; white-space: nowrap;
  }
  .email__at { font-weight: 400; font-size: 22px; margin-right: 6px; }
  .card--dark-left .states, .card--dark-left .email,
  .card--green-right .states, .card--green-right .email { color: var(--grey-text); }
  .card--light-left .states, .card--light-left .email { color: var(--grey-text-dark); }

  .web {
    position: absolute; top: 0; right: 0; height: 320px; width: 90px;
    display: flex; flex-direction: column; align-items: center; justify-content: flex-end;
    padding-bottom: 60px; gap: 14px;
  }
  .web__url {
    writing-mode: vertical-rl; transform: rotate(180deg);
    font-size: 21px; font-weight: 700;
  }
  .web__globe { width: 20px; height: 20px; }
  .card--dark-left .web__url, .card--green-right .web__url { color: var(--ink); }
  .card--light-left .web__url { color: var(--white); }
</style>
</head>
<body>
<main class="sheet">

  <section class="card card--dark-left">
    <svg class="card__shapes" viewBox="0 0 560 320" aria-hidden="true">
      <defs>
        <radialGradient id="darkGlowA" cx="0.1" cy="1" r="0.9">
          <stop offset="0" stop-color="var(--charcoal-warm)"/>
          <stop offset="1" stop-color="var(--charcoal)"/>
        </radialGradient>
        <linearGradient id="paperA" x1="0" y1="0" x2="1" y2="0">
          <stop offset="0" stop-color="var(--paper-shade)"/>
          <stop offset="1" stop-color="var(--paper)"/>
        </linearGradient>
      </defs>
      <rect width="560" height="320" fill="url(#paperA)"/>
      <path d="M0 0H452V190C452 270 420 305 300 320H0Z" fill="var(--green)"/>
      <path d="M0 0H432V200C432 275 400 302 270 320H0Z" fill="url(#darkGlowA)"/>
    </svg>
    <div class="brand"><span class="brand__square"></span><span class="brand__name">KBMR</span></div>
    <ul class="states"><li>Victoria</li><li>New South Wales</li><li>Queensland</li><li>Tasmania</li></ul>
    <p class="email"><span class="email__at">@</span>dan@kbmr.com.au</p>
    <div class="web">
      <span class="web__url">www.kbmr.com.au</span>
      <svg class="web__globe" viewBox="0 0 20 20" aria-hidden="true"><circle cx="10" cy="10" r="8" fill="none" stroke="var(--ink)" stroke-width="2"/><path d="M2 10H18M10 2C6 6 6 14 10 18M10 2C14 6 14 14 10 18" fill="none" stroke="var(--ink)" stroke-width="1.5"/></svg>
    </div>
  </section>

  <section class="card card--light-left">
    <svg class="card__shapes" viewBox="0 0 560 320" aria-hidden="true">
      <defs>
        <radialGradient id="darkGlowB" cx="0.8" cy="1" r="0.5">
          <stop offset="0" stop-color="var(--charcoal-warm)"/>
          <stop offset="1" stop-color="var(--charcoal)"/>
        </radialGradient>
        <radialGradient id="paperB" cx="0.3" cy="0.4" r="0.8">
          <stop offset="0" stop-color="var(--paper)"/>
          <stop offset="1" stop-color="var(--paper-shade)"/>
        </radialGradient>
      </defs>
      <rect width="560" height="320" fill="url(#darkGlowB)"/>
      <path d="M0 0H475V190C475 270 440 305 320 320H0Z" fill="var(--green)"/>
      <path d="M0 0H456V200C456 275 420 302 290 320H0Z" fill="url(#paperB)"/>
    </svg>
    <div class="brand"><span class="brand__square"></span><span class="brand__name">KBMR</span></div>
    <ul class="states"><li>Victoria</li><li>New South Wales</li><li>Queensland</li><li>Tasmania</li></ul>
    <p class="email"><span class="email__at">@</span>dan@kbmr.com.au</p>
    <div class="web">
      <span class="web__url">www.kbmr.com.au</span>
      <svg class="web__globe" viewBox="0 0 20 20" aria-hidden="true"><circle cx="10" cy="10" r="8" fill="none" stroke="var(--white)" stroke-width="2"/><path d="M2 10H18M10 2C6 6 6 14 10 18M10 2C14 6 14 14 10 18" fill="none" stroke="var(--white)" stroke-width="1.5"/></svg>
    </div>
  </section>

  <section class="card card--green-right">
    <svg class="card__shapes" viewBox="0 0 560 320" aria-hidden="true">
      <defs>
        <radialGradient id="darkGlowC" cx="0.1" cy="1" r="0.9">
          <stop offset="0" stop-color="var(--charcoal-warm)"/>
          <stop offset="1" stop-color="var(--charcoal)"/>
        </radialGradient>
        <linearGradient id="greenPanel" x1="0" y1="0" x2="0" y2="1">
          <stop offset="0" stop-color="var(--green)"/>
          <stop offset="1" stop-color="var(--green-bright)"/>
        </linearGradient>
      </defs>
      <rect width="560" height="320" fill="url(#greenPanel)"/>
      <path d="M0 0H455V190C455 270 420 305 300 320H0Z" fill="var(--white)"/>
      <path d="M0 0H440V200C440 275 405 302 275 320H0Z" fill="url(#darkGlowC)"/>
    </svg>
    <div class="brand"><span class="brand__square"></span><span class="brand__name">KBMR</span></div>
    <ul class="states"><li>Victoria</li><li>New South Wales</li><li>Queensland</li><li>Tasmania</li></ul>
    <p class="email"><span class="email__at">@</span>dan@kbmr.com.au</p>
    <div class="web">
      <span class="web__url">www.kbmr.com.au</span>
      <svg class="web__globe" viewBox="0 0 20 20" aria-hidden="true"><circle cx="10" cy="10" r="8" fill="none" stroke="var(--ink)" stroke-width="2"/><path d="M2 10H18M10 2C6 6 6 14 10 18M10 2C14 6 14 14 10 18" fill="none" stroke="var(--ink)" stroke-width="1.5"/></svg>
    </div>
  </section>

</main>
</body>
</html>
```